Two Bodyguards

Cover for a book in French language:
- Author: Mathieu Ferrand-Lacoste
- Title: Cold suspects rarely ever smile back
- Publisher (at the bottom of the page): Editions Vernaille
Key Words:
- a rich man died recently, it looks like a murder. He has been found in his luxury apartment.
- Two Body Guards: one is elegant, the other a bit fat.
- two pretty women.
- Inheritance (wealth)
Size of the cover: 14 x 20.5 cm (+ bleed area)
Please note that the title should remain in English: "Suspects rarely ever smile back".
By the way the title doesn't mean anything. It's just a joke.
Thrillers' reader

```html
<!DOCTYPE html>
<html lang="fr">
<head>
<meta charset="utf-8">
<title>Cold suspects rarely ever smile back — Mathieu Ferrand-Lacoste</title>
<link rel="stylesheet" href="https://fonts.googleapis.com/css2?family=Alfa+Slab+One&family=Montserrat:wght@300;400;600;700&display=swap">
<style>
  :root {
    --page: #ffffff;
    --cover-navy: #1e2536;
    --scene-deep: #1c2334;
    --scene-wall: #2c3446;
    --scene-cushion: #4c4660;
    --scene-floor: #4a5466;
    --scene-floor-light: #6a7282;
    --title-red: #e11b26;
    --title-white: #f6f6f6;
    --text-white: #ffffff;
  }
  * { margin: 0; padding: 0; box-sizing: border-box; }
  html, body {
    width: 1200px;
    height: 1077px;
    overflow: hidden;
    background: var(--page);
  }
  .book-cover {
    position: absolute;
    left: 253px;
    top: 34px;
    width: 681px;
    height: 998px;
    background: var(--cover-navy);
    overflow: hidden;
  }
  .cover-scene {
    position: absolute;
    left: 0;
    top: 400px;
    width: 681px;
    height: 598px;
    background:
      radial-gradient(ellipse 55% 22% at 48% 72%, rgba(150,158,175,0.35), rgba(0,0,0,0) 70%),
      radial-gradient(ellipse 50% 14% at 70% 40%, rgba(110,90,140,0.45), rgba(0,0,0,0) 75%),
      radial-gradient(ellipse 30% 25% at 25% 25%, rgba(90,100,120,0.3), rgba(0,0,0,0) 70%),
      linear-gradient(180deg, var(--cover-navy) 0%, var(--scene-wall) 25%, var(--scene-cushion) 42%, var(--scene-floor) 58%, var(--scene-floor-light) 72%, var(--scene-floor) 88%, var(--scene-wall) 100%);
  }
  .cover-type {
    position: absolute;
    left: 0;
    top: 0;
    width: 681px;
    height: 998px;
  }
  .author-name {
    font-family: "Montserrat", sans-serif;
    font-weight: 600;
    font-size: 31px;
    fill: var(--text-white);
  }
  .title-stamp {
    font-family: "Alfa Slab One", serif;
  }
  .title-red { fill: var(--title-red); }
  .title-white { fill: var(--title-white); }
  .title-link {
    font-family: "Montserrat", sans-serif;
    font-weight: 700;
    font-size: 43px;
    fill: var(--text-white);
  }
  .publisher-name {
    font-family: "Montserrat", sans-serif;
    font-weight: 400;
    font-size: 27px;
    fill: var(--text-white);
  }
</style>
</head>
<body>
  <main class="book-cover">
    <div class="cover-scene" role="img" aria-label="Photograph of a man in a dark suit lying on the tiled floor of a luxury apartment lounge, striped floor cushions and a lamp behind him"></div>

    <svg class="cover-type" viewBox="0 0 681 998" xmlns="http://www.w3.org/2000/svg">
      <defs>
        <filter id="stamp-wear" x="0" y="0" width="100%" height="100%">
          <feTurbulence type="fractalNoise" baseFrequency="0.11" numOctaves="4" seed="7" result="noise"/>
          <feColorMatrix in="noise" type="matrix" result="wear-mask"
            values="0 0 0 0 0
                    0 0 0 0 0
                    0 0 0 0 0
                    -11 0 0 0 7.2"/>
          <feComposite in="SourceGraphic" in2="wear-mask" operator="in"/>
        </filter>
      </defs>

      <text class="author-name" x="91" y="66" textLength="498" lengthAdjust="spacing">MATHIEU FERRAND-LACOSTE</text>

      <g class="title-stamp" filter="url(#stamp-wear)">
        <text class="title-red" x="81" y="228" font-size="146" textLength="516" lengthAdjust="spacingAndGlyphs">COLD</text>
        <text class="title-red" x="81" y="328" font-size="113" textLength="510" lengthAdjust="spacingAndGlyphs">SUSPECTS</text>
        <text class="title-white" x="75" y="508" font-size="149" textLength="522" lengthAdjust="spacingAndGlyphs">SMILE</text>
        <text class="title-white" x="71" y="648" font-size="154" textLength="528" lengthAdjust="spacingAndGlyphs">BACK</text>
      </g>

      <text class="title-link" x="143" y="379" textLength="398" lengthAdjust="spacingAndGlyphs">RARELY EVER</text>

      <text class="publisher-name" x="340.5" y="948" text-anchor="middle">Editions Vernaille</text>
    </svg>
  </main>
</body>
</html>
```